Business Card Design for Marketing Firm

Looking for business card design for higher end marketing firm. Clean but impressionable/trendy. We are a marketing firm that represents manufacturers in the foodservice equipment and supply industry. Our customers are end users such has hotels, restaurants, country clubs, convention centers and casinos as well as distributors of restaurants supplies and equipment, and manufacturers of foodservice equipment and supplies.
Target Market(s)
Hotels, Restaurants, Supply & Equipment Distributors, Foodservice Manufacturers
Industry/Entity Type
Foodservice/Hospitality
Contact Information for Business Card
Name, Title, Contact Number, Email, Website, Social Media, Address
Requirements
Must have
- Clean & Simple but Serious and Impressionable

```html
<!DOCTYPE html>
<html lang="en">
<head>
<meta charset="utf-8">
<title>Harbor Hospitality Reps – Business Card</title>
<link rel="stylesheet" href="https://fonts.googleapis.com/css2?family=Open+Sans:wght@400;600;700&display=swap">
<style>
  :root {
    --navy: #27276c;
    --ink: #1f1f26;
    --paper: #ffffff;
    --page: #ffffff;
    --shadow: rgba(0, 0, 0, 0.28);
  }
  * { box-sizing: border-box; margin: 0; padding: 0; }
  html, body {
    width: 864px; height: 1200px; overflow: hidden;
    background: var(--page);
    font-family: "Open Sans", Arial, sans-serif;
  }
  .canvas { position: relative; width: 864px; height: 1200px; }

  .card {
    position: absolute; left: 112px;
    width: 640px; height: 365px;
    box-shadow: 0 8px 14px var(--shadow);
    overflow: hidden;
  }
  .card--front { top: 170px; background: var(--paper); }
  .card--back  { top: 640px; background: var(--navy); }

  /* front */
  .accent-bar { position: absolute; top: 40px; width: 13px; height: 55px; background: var(--navy); }
  .accent-bar--left { left: 0; }
  .accent-bar--right { right: 0; }
  .holder-name {
    position: absolute; left: 49px; top: 52px;
    font-size: 28px; font-weight: 700; color: var(--ink); letter-spacing: -0.2px;
  }
  .name-rule { position: absolute; left: 29px; right: 29px; top: 112px; height: 3px; background: var(--navy); }
  .contact-list { position: absolute; left: 50px; top: 160px; list-style: none; }
  .contact-item {
    display: flex; align-items: center; height: 35px;
    font-size: 19px; color: var(--ink); font-weight: 400;
  }
  .contact-item strong { font-weight: 600; }
  .contact-icon { width: 15px; height: 15px; margin-right: 20px; fill: var(--navy); flex: none; }
  .footer-band { position: absolute; left: 0; right: 0; bottom: 0; height: 17px; background: var(--navy); }

  .wordmark {
    position: absolute; text-align: center;
    font-weight: 600; letter-spacing: 2px; line-height: 1.25;
  }
  .wordmark--front { left: 380px; width: 230px; top: 190px; font-size: 17px; color: var(--navy); }
  .wordmark--back  { left: 0; right: 0; top: 148px; font-size: 22px; color: #ffffff; }
  .wordmark small { display: block; font-size: 0.6em; letter-spacing: 4px; }

  .back-url {
    position: absolute; left: 0; right: 0; bottom: 26px; text-align: center;
    font-size: 14px; color: #ffffff;
  }
</style>
</head>
<body>
<main class="canvas">
  <section class="card card--front" aria-label="Business card front">
    <div class="accent-bar accent-bar--left"></div>
    <div class="accent-bar accent-bar--right"></div>
    <h1 class="holder-name">YOUR NAME</h1>
    <div class="name-rule"></div>
    <ul class="contact-list">
      <li class="contact-item">
        <svg class="contact-icon" viewBox="0 0 16 16"><path d="M8 0a8 8 0 1 0 0 16A8 8 0 0 0 8 0zm5.9 7H11a12 12 0 0 0-1-4.6A6 6 0 0 1 13.9 7zM8 2c.8 1 1.5 2.9 1.6 5H6.4C6.5 4.9 7.2 3 8 2zM6 2.4A12 12 0 0 0 5 7H2.1A6 6 0 0 1 6 2.4zM2.1 9H5a12 12 0 0 0 1 4.6A6 6 0 0 1 2.1 9zM8 14c-.8-1-1.5-2.9-1.6-5h3.2C9.5 11.1 8.8 13 8 14zm2 -.4A12 12 0 0 0 11 9h2.9a6 6 0 0 1-3.9 4.6z"/></svg>
        www.sampletext.com
      </li>
      <li class="contact-item">
        <svg class="contact-icon" viewBox="0 0 16 16"><path d="M0 3h16v1.2L8 9 0 4.2z"/><path d="M0 6l8 4.8L16 6v7H0z"/></svg>
        sampletext@mailbox.com
      </li>
      <li class="contact-item">
        <svg class="contact-icon" viewBox="0 0 16 16"><path d="M8 0a5.5 5.5 0 0 0-5.5 5.5C2.5 10 8 16 8 16s5.5-6 5.5-10.5A5.5 5.5 0 0 0 8 0zm0 7.7a2.2 2.2 0 1 1 0-4.4 2.2 2.2 0 0 1 0 4.4z"/></svg>
        Address_<strong>sampletext</strong>
      </li>
      <li class="contact-item">
        <svg class="contact-icon" viewBox="0 0 16 16"><path d="M3.6 0.5l2.4 3.2-1.5 2c.9 2.3 2.6 4.1 5 5l2-1.5 3.2 2.4-1.7 3.2C7 14.5 1.5 9 .6 2.2z"/></svg>
        000-000-000
      </li>
    </ul>
    <div class="wordmark wordmark--front">HARBOR HOSPITALITY<small>REPS</small></div>
    <div class="footer-band"></div>
  </section>

  <section class="card card--back" aria-label="Business card back">
    <div class="wordmark wordmark--back">HARBOR HOSPITALITY<small>REPS</small></div>
    <div class="back-url">www.sampletext.com</div>
  </section>
</main>
</body>
</html>
```